Startup photo studio needs full suite design (logo, business cards, etc) starting with a website.

We need a website designed for a startup photo studio in the Sacramento area called Silver Lantern Photo Studio. We do portrait work, specializing in the male form and are looking to get into editorial. We would also like to be able to sell prints, posters and canvasses of our work. I would like an elegant but fun design. One of the most important things a portrait photographer needs is the trust of the model. The website would convey honesty, friendliness and warmth as well. I have a domain name with NetHarbor, silverlanternstudio.example email address should be my name with that domain.

Target Market(s)

Art enthusiasts, business portraits, online dating photos

Industry/Entity Type

Professional Photography

Contact Information for Business Card

Simple please. Just logo and contact info. Phone, email, website. no address required

Logo Text

Silver Lantern Photo Studio --- light tells the story

Number of Pages Required

3 page

Font styles to use
Sans Serif

Colors

Designer to choose colors to be used in the design.

Requirements
Must have
• Simple clean design.
Nice to have
• Somehow one of my photos in the design? maybe not...
Should not have
• No weddings!

```html
<!DOCTYPE html>
<html lang="en">
<head>
<meta charset="utf-8">
<title>Silver Lantern Photo Studio</title>
<link href="https://fonts.googleapis.com/css2?family=Montserrat:wght@300;400;600;700&display=swap" rel="stylesheet">
<style>
:root{
  --teal:#1fb3c4;
  --navy:#1c2a38;
  --ink:#222;
  --dark:#0e0e0e;
  --grey:#555;
  --paper:#fff;
  --stage:#e6e6e6;
  --gold:#c9a25a;
}
*{margin:0;padding:0;box-sizing:border-box}
html,body{width:1200px;height:1200px;overflow:hidden;background:var(--stage);font-family:'Montserrat',sans-serif}
.board{position:absolute;left:0;top:0;width:1500px;height:1500px;transform:scale(.8);transform-origin:0 0}
.page{position:absolute;left:616px;top:0;width:267px;height:1500px;background:var(--paper);box-shadow:0 0 30px rgba(0,0,0,.35);overflow:hidden}
.abs{position:absolute}
.photo{position:absolute}
.tiny{font-size:3px;line-height:4.4px;color:var(--grey)}
.title{position:absolute;left:0;width:100%;text-align:center;font-size:7.5px;letter-spacing:.4px;color:var(--ink)}
.title b{color:var(--teal);font-weight:700}
.lead{position:absolute;left:30px;width:207px;text-align:center;font-size:2.6px;line-height:4px;color:var(--grey)}
.btn{position:absolute;background:var(--teal);color:#fff;font-size:2.6px;text-align:center;border-radius:6px;letter-spacing:.3px}

/* nav */
.nav{position:absolute;left:0;top:0;width:267px;height:21px;background:var(--navy)}
.brand-name{position:absolute;font-size:4.5px;color:#fff;font-weight:600;white-space:nowrap}
.nav .brand-name{left:10px;top:8px}
.nav ul{position:absolute;left:96px;top:0;display:flex;list-style:none;height:21px}
.nav li{font-size:2.6px;color:#dfe6ec;padding:9px 3px 0;text-transform:uppercase}
.nav li.on{background:var(--teal);color:#fff}

/* hero */
.hero{left:0;top:21px;width:267px;height:117px;background:linear-gradient(120deg,#3a1c14 0%,#7b2b1e 35%,#2b3b55 75%,#14213a 100%)}
.hero h1{position:absolute;left:12px;top:12px;font-weight:400;font-size:12px;color:#fff}
.hero h2{position:absolute;left:12px;top:27px;font-weight:700;font-size:16px;color:var(--teal);letter-spacing:.3px}
.hero p{position:absolute;left:12px;top:50px;font-size:7px;letter-spacing:2.2px;color:#f0e9e2}
.hero .pager{position:absolute;left:224px;top:30px;width:7px;height:36px;border:1px solid #fff;border-radius:4px}
.hero .pager i{display:block;width:1px;height:5px;background:#fff;margin:5px auto}
.band{left:0;top:137px;width:267px;height:2px;background:var(--teal)}

/* frames */
.frame{position:absolute;border-left:1px solid #999;border-top:1px solid #999}
.frame2{position:absolute;border-right:1px solid #999;border-bottom:1px solid #999}

.about .h{left:156px;top:159px;font-size:7.5px;color:var(--ink)}
.about .h b{color:var(--teal)}
.social{position:absolute;left:156px;top:268px;display:flex;gap:3px}
.social i{width:6px;height:6px;border-radius:50%;background:#222}

.svc{position:absolute;top:437px;width:76px;text-align:center}
.svc h4{font-size:4.6px;font-weight:400;color:#444}
.svc p{font-size:2.5px;line-height:3.8px;color:#777;margin-top:3px}
.svc em{display:block;font-style:normal;font-size:2.5px;color:var(--teal);margin-top:2px}

.work{left:0;top:495px;width:267px;height:153px;background:var(--dark)}
.work h3{position:absolute;left:12px;top:28px;width:100px;font-size:7px;font-weight:400;color:#fff;text-align:center}
.work h3 b{display:block;color:var(--teal);font-weight:700;margin-top:-1px}
.work .txt{position:absolute;left:12px;top:52px;width:96px;color:#ccc}

.tabs{position:absolute;left:77px;top:706px;display:flex;gap:1px}
.tabs span{font-size:2.3px;color:#fff;background:#333;padding:1.5px 3px}
.tabs span.on{background:var(--teal)}

.feedback{left:0;top:866px;width:267px;height:152px;background:linear-gradient(90deg,#121212,#2a211c 60%,#151515)}
.feedback .title{color:#fff}
.feedback .name{position:absolute;left:115px;top:72px;font-size:4px;color:var(--teal);letter-spacing:.5px}
.feedback .arr{position:absolute;top:92px;font-size:6px;color:#fff}

.card{position:absolute;top:1085px;width:76px;height:133px;background:var(--teal);overflow:hidden}
.card.mid{background:#2b2b2b}
.card .top{position:absolute;left:0;top:0;width:76px;height:22px;background:#2b2b2b}
.card.mid .top{background:var(--teal)}
.card .disc{position:absolute;left:22px;top:9px;width:32px;height:32px;border-radius:50%;background:#333;border:1.5px solid #fff;color:#fff;text-align:center}
.card.mid .disc{background:var(--teal)}
.card .disc small{display:block;font-size:2.2px;margin-top:9px}
.card .disc strong{display:block;font-size:5px}
.card ul{position:absolute;left:4px;top:47px;width:68px;list-style:none;text-align:center}
.card li{font-size:2.3px;color:#fff;line-height:3.6px;margin-bottom:2.6px}
.card .buy{position:absolute;left:18px;top:113px;width:40px;height:7px;background:#222;color:#fff;font-size:2.3px;text-align:center;line-height:7px;border-radius:4px}
.card.mid .buy{background:var(--teal)}
.card .cut{position:absolute;left:0;bottom:0}

.news{left:0;top:1240px;width:267px;height:91px;background:var(--teal)}
.news .title{color:#e9fbfd}
.news .title b{color:#fff}
.field{position:absolute;left:76px;top:59px;width:82px;height:8px;background:#fff;border-radius:4px 0 0 4px;font-size:2.3px;color:#aaa;text-align:center;line-height:8px}
.sub{position:absolute;left:158px;top:59px;width:35px;height:8px;background:var(--navy);color:#fff;border-radius:0 4px 4px 0;font-size:2.3px;text-align:center;line-height:8px}

.contact{left:0;top:1331px;width:267px;height:157px;background:linear-gradient(180deg,#1f2933,#27313c)}
.contact .title{color:#fff}
.contact .brand-name{left:13px;top:59px}
.contact .info{position:absolute;left:13px;top:72px;width:80px;color:#cfd6dc}
.input{position:absolute;left:158px;width:96px;border-bottom:.5px solid #8996a3;font-size:2.3px;color:#aab4be;height:7px}
.send{position:absolute;left:158px;top:120px;width:36px;height:8px;background:var(--teal);color:#fff;font-size:2.3px;text-align:center;line-height:8px}
.foot{left:0;top:1488px;width:267px;height:12px;background:#121a22}
.foot p{position:absolute;left:0;width:100%;top:4px;text-align:center;font-size:2.3px;color:#9aa5af}
.foot i{position:absolute;right:4px;top:1px;width:9px;height:10px;background:var(--teal)}
</style>
</head>
<body>
<div class="board">
<div class="page">

  <nav class="nav">
    <div class="brand-name">Silver Lantern</div>
    <ul><li class="on">Home</li><li>About us</li><li>Services</li><li>Portfolio</li><li>Feedback</li><li>Pricing</li><li>Contact us</li></ul>
  </nav>

  <section class="abs hero" role="img" aria-label="Hero photograph: woman holding a camera to her face, warm red and deep blue tones">
    <h1>We Are Best</h1>
    <h2>PHOTOGRAPHER</h2>
    <p>&amp; Award Winner 2016</p>
    <div class="btn" style="left:12px;top:91px;width:42px;height:6px;line-height:6px">VIEW OUR WORK</div>
    <div class="pager"><i></i><i></i></div>
  </section>
  <div class="abs band"></div>

  <section class="about">
    <div class="frame" style="left:12px;top:160px;width:60px;height:60px"></div>
    <div class="frame2" style="left:70px;top:230px;width:60px;height:60px"></div>
    <div class="photo" role="img" aria-label="Portrait of a curly-haired woman aiming a camera" style="left:18px;top:166px;width:106px;height:119px;background:linear-gradient(160deg,#e8ddd2,#b88a6e 55%,#4a2e22)"></div>
    <div class="abs h">[ABOUT <b>US</b>]</div>
    <div class="abs" style="left:156px;top:176px;width:90px;font-size:4px;line-height:4.6px;color:#222">We are excellent photographer and creative designer.</div>
    <div class="abs tiny" style="left:156px;top:198px;width:98px;font-size:2.5px;line-height:3.8px">Silver Lantern began as a small studio built on trust. We take time to know every model so each session feels relaxed, honest and warm from start to finish.<br><br>Our portraits celebrate the person in front of the lens. We work with natural light, calm direction and careful editing to create images that feel true, confident and lasting for you.</div>
    <div class="abs" style="left:156px;top:257px;font-size:2.8px;color:#222">Silver Lantern Studio</div>
    <div class="abs" style="left:156px;top:262px;width:38px;border-top:.5px solid #999"></div>
    <div class="social"><i></i><i></i><i></i><i></i></div>
  </section>

  <section>
    <div class="title" style="top:311px">[WE PROVIDE <b>THE BEST SERVICES</b>]</div>
    <div class="lead" style="top:327px">Lorem ipsum is simply sample text of the printing and typesetting trade used as filler for layouts since long ago by designers and printers everywhere.</div>

    <div class="frame" style="left:12px;top:349px;width:30px;height:30px"></div>
    <div class="frame2" style="left:54px;top:398px;width:30px;height:30px"></div>
    <div class="photo" role="img" aria-label="Couple portrait photograph" style="left:16px;top:353px;width:68px;height:72px;background:linear-gradient(135deg,#cfd6dc,#6b7480 60%,#2c2f36)"></div>
    <div class="frame" style="left:94px;top:349px;width:30px;height:30px"></div>
    <div class="frame2" style="left:136px;top:398px;width:30px;height:30px"></div>
    <div class="photo" role="img" aria-label="Corporate team photograph in an office" style="left:98px;top:353px;width:68px;height:72px;background:linear-gradient(135deg,#e9ecef,#a7b3bf 55%,#4e5966)"></div>
    <div class="frame" style="left:177px;top:349px;width:30px;height:30px"></div>
    <div class="frame2" style="left:219px;top:398px;width:30px;height:30px"></div>
    <div class="photo" role="img" aria-label="Seated portrait session photograph" style="left:181px;top:353px;width:68px;height:72px;background:linear-gradient(135deg,#3b4a3e,#8a6b70 55%,#c8495f)"></div>

    <div class="svc" style="left:12px"><h4>Couple Photography</h4><p>Sample text for the service card giving a short note about what this session includes and how it feels.</p><em>Read More...</em></div>
    <div class="svc" style="left:94px"><h4>Corporate Photography</h4><p>Sample text for the service card giving a short note about what this session includes and how it feels.</p><em>Read More...</em></div>
    <div class="svc" style="left:177px"><h4>Portraits Photography</h4><p>Sample text for the service card giving a short note about what this session includes and how it feels.</p><em>Read More...</em></div>
  </section>

  <section class="abs work">
    <h3>[ &nbsp; OUR AWSOME &nbsp; ]<b>WORK</b></h3>
    <div class="txt tiny" style="font-size:2.5px;line-height:3.9px">Sample text describing our favourite sessions, the people we photograph and the care we bring to every frame we make.<br><br>Sample text describing our editorial plans, print work and the stories we want to tell with light.</div>
    <div class="btn" style="left:12px;top:106px;width:46px;height:8px;line-height:8px">SEE MORE WORK</div>
    <svg class="abs" style="left:126px;top:15px" width="120" height="120" viewBox="0 0 120 120">
      <circle cx="60" cy="60" r="58" fill="none" stroke="#3a3020" stroke-width="1"/>
      <circle cx="60" cy="60" r="54" fill="none" stroke="var(--gold)" stroke-width="1.5"/>
    </svg>
    <div class="photo" role="img" aria-label="Circular collage of fashion and portrait photographs" style="left:134px;top:23px;width:104px;height:104px;border-radius:50%;background:linear-gradient(135deg,#c9a27a,#6e4b5e 45%,#2b2b3a 70%,#a58a6a)"></div>
  </section>

  <section>
    <div class="title" style="top:668px">[OUR AWESOME <b>PORTFOLIO</b>]</div>
    <div class="lead" style="top:685px">Sample text about the portfolio, a short line on the kinds of sessions shown and how to browse them below.</div>
    <div class="tabs"><span class="on">CATEGORY</span><span>PORTRAITS</span><span>FASHION</span><span>EDITORIAL PRINTS</span></div>

    <div class="photo" role="img" aria-label="Studio portrait on a couch" style="left:2px;top:727px;width:61px;height:63px;background:linear-gradient(160deg,#8fa6ad,#3c5560)"></div>
    <div class="photo" role="img" aria-label="Couple portrait" style="left:69px;top:727px;width:127px;height:63px;background:linear-gradient(120deg,#e0c6a8,#9a7a5e 50%,#3b3b44)"></div>
    <div class="photo" role="img" aria-label="Colourful dance portrait" style="left:203px;top:727px;width:61px;height:63px;background:linear-gradient(160deg,#bfe3ee,#d0608a 55%,#4b6cb8)"></div>
    <div class="photo" role="img" aria-label="Group fashion portrait" style="left:2px;top:796px;width:61px;height:64px;background:linear-gradient(160deg,#7d7068,#2a2422)"></div>
    <div class="photo" role="img" aria-label="Editorial group portrait" style="left:69px;top:796px;width:61px;height:64px;background:linear-gradient(160deg,#c9c2b8,#4d4440)"></div>
    <div class="photo" role="img" aria-label="Male portrait in blue tank top" style="left:135px;top:796px;width:61px;height:64px;background:linear-gradient(160deg,#151515,#2f5fb0 60%,#111)"></div>
    <div class="photo" role="img" aria-label="Male figure study" style="left:203px;top:796px;width:61px;height:64px;background:linear-gradient(160deg,#111,#8a6a4a 55%,#111)"></div>
  </section>

  <section class="abs feedback" role="img" aria-label="Dark studio backdrop with client testimonial">
    <div class="title" style="top:20px">[CLIENT <b>FEEDBACK</b>]</div>
    <div class="lead" style="top:37px;color:#bbb">Sample text introducing what our clients say after their sessions with the studio team.</div>
    <div class="frame" style="left:12px;top:59px;width:30px;height:30px;border-color:#bbb"></div>
    <div class="frame2" style="left:54px;top:101px;width:30px;height:30px;border-color:#bbb"></div>
    <div class="photo" role="img" aria-label="Client portrait photograph" style="left:17px;top:64px;width:67px;height:63px;background:linear-gradient(150deg,#d8d2cc,#b1403a 60%,#3a2b28)"></div>
    <div class="name">ELENA MARSH</div>
    <div class="abs tiny" style="left:115px;top:77px;font-size:2.3px;color:#999">Model</div>
    <div class="abs tiny" style="left:115px;top:88px;width:140px;font-size:2.5px;line-height:3.9px;color:#ccc">The team made me feel at ease from the first minute. The session was fun, honest and relaxed, and the final portraits are the best I have ever had taken of me.</div>
    <div class="abs" style="left:115px;top:112px;font-size:4px;color:var(--gold);letter-spacing:1.5px">★★★★★</div>
    <div class="arr" style="left:3px">‹</div>
    <div class="arr" style="left:258px">›</div>
  </section>

  <section>
    <div class="title" style="top:1046px">[PURCHASE <b>A PACKAGE</b>]</div>
    <div class="lead" style="top:1063px">Sample text about our session packages, what each one offers and how to book the one that fits you best.</div>

    <div class="card" style="left:14px">
      <div class="top"></div>
      <div class="disc"><small>PROFESSIONAL</small><strong>$450</strong></div>
      <ul><li>✔ Final images fully retouched</li><li>✔ Print release for personal use and sharing</li><li>✔ 50 edited high resolution images</li><li>✔ Two hour session of studio or outdoor portraits</li><li>✔ Online private gallery of all images</li><li>✔ Travel fees may apply</li></ul>
      <div class="buy">Purchase Now</div>
      <svg class="cut" width="76" height="10"><polygon points="0,10 76,0 76,10" fill="#2b2b2b"/></svg>
    </div>
    <div class="card mid" style="left:96px">
      <div class="top"></div>
      <div class="disc"><small>PORTFOLIO</small><strong>$450</strong></div>
      <ul><li>✔ Final images fully retouched</li><li>✔ Print release for personal use and sharing</li><li>✔ 50 edited high resolution images</li><li>✔ Two hour session of studio or outdoor portraits</li><li>✔ Online private gallery of all images</li><li>✔ Travel fees may apply</li></ul>
      <div class="buy">Purchase Now</div>
      <svg class="cut" width="76" height="10"><polygon points="0,10 76,0 76,10" fill="#3a3a3a"/></svg>
    </div>
    <div class="card" style="left:178px">
      <div class="top"></div>
      <div class="disc"><small>EDITORIAL</small><strong>$450</strong></div>
      <ul><li>✔ Final images fully retouched</li><li>✔ Print release for personal use and sharing</li><li>✔ 50 edited high resolution images</li><li>✔ Two hour session of studio or outdoor portraits</li><li>✔ Online private gallery of all images</li><li>✔ Travel fees may apply</li></ul>
      <div class="buy">Purchase Now</div>
      <svg class="cut" width="76" height="10"><polygon points="0,10 76,0 76,10" fill="#2b2b2b"/></svg>
    </div>
  </section>

  <section class="abs news">
    <div class="title" style="top:20px">[5000K PEOPLE LIKE <b>US</b>]</div>
    <div class="lead" style="top:37px;color:#e5f7f9">Sample text inviting visitors to join our list for print releases, studio news and booking dates.</div>
    <div class="field">Enter Your Email</div>
    <div class="sub">SUBSCRIBE</div>
  </section>

  <section class="abs contact" role="img" aria-label="Dark map backdrop behind contact details">
    <div class="title" style="top:24px">[CONTACTS <b>US</b>]</div>
    <div class="lead" style="top:41px;color:#b9c2cb">Sample text inviting you to get in touch for bookings, prints and editorial work with our studio team.</div>
    <div class="brand-name">Silver Lantern</div>
    <div class="info tiny" style="font-size:2.5px;line-height:4px">Address<br>Sacramento, CA<br><br>Email: hello@silverlanternstudio.example<br>Phone: (916) 555-0148</div>
    <div class="abs" style="left:13px;top:106px;display:flex;gap:3px"><i style="width:4px;height:4px;border-radius:50%;background:#6d7883"></i><i style="width:4px;height:4px;border-radius:50%;background:#6d7883"></i><i style="width:4px;height:4px;border-radius:50%;background:#6d7883"></i><i style="width:4px;height:4px;border-radius:50%;background:#6d7883"></i><i style="width:4px;height:4px;border-radius:50%;background:#6d7883"></i></div>
    <div class="input" style="top:58px">Name</div>
    <div class="input" style="top:69px">Email</div>
    <div class="input" style="top:80px">Phone</div>
    <div class="input" style="top:91px;height:24px">Message</div>
    <div class="send">SEND MESSAGE</div>
  </section>

  <footer class="abs foot"><p>Copyright © 2017 All Right Reserved. Silver Lantern Photo Studio</p><i></i></footer>

</div>
</div>
</body>
</html>
```